Bramble Nook Complementary Pass

I’d like a complimentary pass for any 30-minute Bramble Nook session. Choose one of the following options: Infrared Sauna with Red Light, Massage Chair Velquist Compression Therapy, or Paraffin Wax Hand Bath.

Please incorporate the logo and brand colors into your design. I’d like a square image that will be printed on square business cards (no rectangles).

Please refer to the logo and menu for more details.

See discretion

```html
<!DOCTYPE html>
<html lang="en">
<head>
<meta charset="UTF-8">
<title>Solvane Physical Therapy – Bramble Nook Complimentary Pass</title>
<link rel="stylesheet" href="https://fonts.googleapis.com/css2?family=Saira:wght@500;600;700&family=Saira+Condensed:wght@700&display=swap">
<style>
  :root {
    --stage: #4a2777;
    --card-purple: #3e2586;
    --card-cream: #f4f0e9;
    --accent-orange: #e2673f;
    --ink-navy: #33207a;
    --text-light: #f6f2ec;
  }
  * { box-sizing: border-box; margin: 0; padding: 0; }
  html, body {
    width: 1200px; height: 901px; overflow: hidden;
    background: var(--stage);
  }
  .stage {
    position: relative; width: 1200px; height: 901px;
    display: flex; align-items: center; justify-content: center; gap: 60px;
  }
  .card {
    width: 460px; height: 460px; border-radius: 42px;
    display: flex; flex-direction: column; align-items: center; justify-content: center;
    text-align: center; font-family: "Saira", sans-serif;
  }
  .card--back { background: var(--card-cream); color: var(--ink-navy); }
  .card--front { background: var(--card-purple); color: var(--text-light); }

  .brand-mark {
    display: flex; align-items: center; gap: 12px;
    font-family: "Saira", sans-serif; font-weight: 600;
  }
  .brand-mark__dot { border-radius: 50%; background: var(--accent-orange); }
  .card--back .brand-mark { color: var(--accent-orange); font-size: 30px; margin-bottom: 14px; }
  .card--back .brand-mark__dot { width: 22px; height: 22px; }
  .card--front .brand-mark { font-size: 72px; line-height: 1; }
  .card--front .brand-mark__dot { width: 40px; height: 40px; }

  .section-title {
    color: var(--accent-orange); font-weight: 700; font-size: 27px;
    letter-spacing: 1px; margin-bottom: 6px;
  }
  .option-list, .contact-list { list-style: none; font-weight: 600; font-size: 18px; line-height: 1.4; }
  .option-list { margin-bottom: 22px; }

  .tagline {
    font-family: "Saira Condensed", sans-serif; font-weight: 700;
    font-size: 27px; letter-spacing: 2px; margin: 14px 0 34px;
  }
  .pass-details { font-weight: 600; font-size: 20px; letter-spacing: 1px; line-height: 1.2; }
  .pass-details__rule { width: 210px; height: 2px; background: var(--accent-orange); margin: 8px auto; }
</style>
</head>
<body>
<main class="stage">
  <section class="card card--back" aria-label="Pass back: options and contact">
    <div class="brand-mark"><span class="brand-mark__dot"></span>Solvane</div>
    <h2 class="section-title">CHOOSE ONE</h2>
    <ul class="option-list">
      <li>Infrared Sauna + Red Light</li>
      <li>Velquist Compression Therapy</li>
      <li>Paraffin Wax Hand Bath</li>
      <li>Massage Chair</li>
    </ul>
    <h2 class="section-title">CONTACT US</h2>
    <ul class="contact-list">
      <li>000 000-0000</li>
      <li>hello@solvanept.com</li>
      <li>www.solvanept.com</li>
      <li>56 Harbor Lane 20</li>
      <li>Your City, ST 00000</li>
    </ul>
  </section>

  <section class="card card--front" aria-label="Pass front">
    <div class="brand-mark"><span class="brand-mark__dot"></span>solvane</div>
    <p class="tagline">PHYSICAL THERAPY</p>
    <div class="pass-details">
      <p>Bramble Nook</p>
      <div class="pass-details__rule"></div>
      <p>Complimentary Pass</p>
      <div class="pass-details__rule"></div>
      <p>Any 30-minute Bramble Nook<br>session</p>
    </div>
  </section>
</main>
</body>
</html>
```